Business Card Design Can you design a business card design? Looking for something unique and differe

Can you design a business card design? Looking for something unique and different. Can you design a business card design? Looking for something unique and different.Can you design a business card design? Looking for something unique and different.Can you design a business card design? Looking for something unique and different.Can you design a business card design? Looking for something unique and different.Can you design a business card design? Looking for something unique and different.

Industry/Entity Type

Business

Contact Information for Business Card

Can you design a business card design? Looking for something unique and different.

Font styles to use
Serif

```html
<!DOCTYPE html>
<html lang="en">
<head>
<meta charset="UTF-8">
<title>Corvalis Business Card</title>
<link rel="stylesheet" href="https://fonts.googleapis.com/css2?family=Questrial&display=swap">
<style>
  :root {
    --backdrop: #e8e2d4;
    --card-white: #f4f3f1;
    --brand-purple: #8a5ad9;
    --card-grey: #6a6a6a;
    --text-grey: #4a4a4a;
    --rule-grey: #9a9a9a;
    --white: #ffffff;
  }
  html, body {
    margin: 0;
    padding: 0;
    width: 1200px;
    height: 927px;
    overflow: hidden;
    background: var(--backdrop);
    font-family: "Questrial", "Century Gothic", sans-serif;
  }
  .canvas {
    position: relative;
    width: 1200px;
    height: 927px;
  }
  .hex-card {
    position: absolute;
    width: 500px;
    height: 433px;
    clip-path: polygon(25% 0, 75% 0, 100% 50%, 75% 100%, 25% 100%, 0 50%);
  }
  .card-front {
    left: 80px;
    top: 262px;
    background: var(--card-white);
  }
  .card-back {
    left: 630px;
    top: 232px;
    background: var(--card-grey);
  }
  .brand {
    position: absolute;
    top: 78px;
    left: 0;
    width: 100%;
    text-align: center;
  }
  .brand-name {
    display: block;
    font-size: 64px;
    line-height: 1;
    color: var(--brand-purple);
    letter-spacing: 1px;
  }
  .brand-tagline {
    display: inline-flex;
    align-items: center;
    gap: 10px;
    margin-top: 6px;
    font-size: 14px;
    letter-spacing: 5px;
    color: var(--text-grey);
  }
  .brand-tagline::before,
  .brand-tagline::after {
    content: "";
    width: 34px;
    height: 1px;
    background: var(--rule-grey);
  }
  .name-band {
    position: absolute;
    top: 200px;
    left: 0;
    width: 100%;
    height: 82px;
    background: var(--brand-purple);
    color: var(--white);
    text-align: center;
    box-sizing: border-box;
    padding-top: 14px;
  }
  .person-name {
    display: block;
    font-size: 28px;
    letter-spacing: 1.5px;
    text-transform: uppercase;
  }
  .person-title {
    display: block;
    font-size: 20px;
    margin-top: 2px;
  }
  .contact-list {
    position: absolute;
    top: 300px;
    left: 118px;
    margin: 0;
    padding: 0;
    list-style: none;
    font-size: 19px;
    line-height: 30px;
    color: var(--text-grey);
  }
  .contact-label {
    color: var(--brand-purple);
    margin-right: 6px;
  }
  .back-mark {
    position: absolute;
    inset: 0;
    display: flex;
    align-items: center;
    justify-content: center;
    gap: 18px;
  }
  .back-dot {
    width: 34px;
    height: 34px;
    border-radius: 50%;
    background: var(--brand-purple);
  }
  .back-name {
    font-size: 72px;
    color: var(--white);
    letter-spacing: 1px;
  }
</style>
</head>
<body>
  <main class="canvas">
    <section class="hex-card card-front">
      <div class="brand">
        <span class="brand-name">Corvalis</span>
        <span class="brand-tagline">cost management</span>
      </div>
      <div class="name-band">
        <span class="person-name">Dalton Whitmore</span>
        <span class="person-title">President</span>
      </div>
      <ul class="contact-list">
        <li><span class="contact-label">E:</span>dalton.whitmore@example.com</li>
        <li><span class="contact-label">T:</span>555-201-0147</li>
        <li><span class="contact-label">F:</span>555-201-0183</li>
      </ul>
    </section>
    <section class="hex-card card-back">
      <div class="back-mark">
        <span class="back-dot"></span>
        <span class="back-name">Corvalis</span>
      </div>
    </section>
  </main>
</body>
</html>
```